Company Employee Onboarding Presentation

We need a custom PowerPoint design for a company presentation. This presentation will be sent to new employees during their onboarding/hiring process. We have attached a current mock-up of the presentation - but this is for content only. We do not like the style of the mock-up. We're a commercial real estate investment company based in Los Angeles, CA. Our website is: www.marnwickhold.com.

One artistic element that we want in the presentation is that we want a timeline similar to the attached file, but want to overlay a rising bar chart from left to right that shows the total number of units owned rising through the years. We would like this to be in the background though by using a low opacity value for the color of the graph. A great example of what we want the timeline to look like is at the bottom of the following webpage (we would just need to add the rising bar chart in the background). https://www.tolvercastlecap.com/firm. This timeline is what would take the place of page 4 of the attached PP presentation.

In addition to our company landing page, the following website is representative of a style we like: https://www.qeo.com

```html
<!DOCTYPE html>
<html lang="en">
<head>
<meta charset="utf-8">
<title>The Marnwick Group – Onboarding Presentation</title>
<link href="https://fonts.googleapis.com/css2?family=Rubik:wght@400;500;600;700&family=Open+Sans:wght@400;600;700&display=swap" rel="stylesheet">
<style>
:root{
  --red:#b01a2b;
  --red-dark:#7e0f1c;
  --red-soft:#d9475a;
  --ink:#1f1f23;
  --body:#4a4a50;
  --muted:#6d6d74;
  --card:#e9eaee;
  --page:#c9cacc;
  --bar:#dbe8f4;
  --white:#ffffff;
}
*{margin:0;padding:0;box-sizing:border-box}
html,body{width:1200px;height:4789px;overflow:hidden;background:var(--page)}
body{position:relative;font-family:"Open Sans",Arial,sans-serif;color:var(--body)}
.slide{position:absolute;left:45px;width:1110px;height:623px;background:var(--white);overflow:hidden}
.decor{position:absolute;inset:0;width:100%;height:100%}
.abs{position:absolute}
.brand{position:absolute;right:26px;top:24px;font-family:"Rubik",sans-serif;font-weight:500;font-size:30px;color:var(--ink);display:flex;align-items:center;gap:10px}
.brand::before{content:"";width:14px;height:14px;background:var(--red)}
.slide-title{position:absolute;left:0;right:0;text-align:center;font-family:"Rubik",sans-serif;font-weight:500;font-size:34px;color:var(--red)}
.slide-title.upper{text-transform:uppercase;font-weight:600;letter-spacing:.5px}
.divider{position:absolute;left:50%;transform:translateX(-50%);display:flex;gap:5px;align-items:center}
.divider i{display:block;width:5px;height:3px;background:#e3a4ab}
.divider i:nth-child(2){width:6px;height:6px;background:var(--red)}

/* Welcome */
.welcome{top:41px;background:linear-gradient(120deg,#c41f33,var(--red-dark))}
.welcome-text{position:absolute;left:745px;top:180px;width:340px;text-align:center;color:var(--white);font-family:"Rubik",sans-serif}
.welcome-text .kicker{font-size:38px;font-weight:400;letter-spacing:1px}
.welcome-text .name{font-size:42px;font-weight:500;margin-top:18px}
.welcome-text .tag{font-family:"Open Sans",sans-serif;font-size:14px;font-weight:600;margin-top:24px}
.follow{position:absolute;left:688px;top:570px;display:flex;align-items:center;gap:14px;color:var(--white);font-family:"Rubik",sans-serif;font-size:22px}
.follow .rule{width:185px;height:2px;background:var(--white)}
.follow .dot{width:16px;height:16px;border:2px solid var(--white);border-radius:50%}

/* Who we are */
.who{top:715px}
.intro{position:absolute;left:173px;width:764px;top:140px;text-align:center;font-size:13px;line-height:19px;color:var(--body)}
.lead{position:absolute;left:0;right:0;top:232px;text-align:center;font-size:13px;font-weight:700;color:var(--red)}
.beliefs{position:absolute;left:234px;top:268px;list-style:none;width:820px}
.beliefs li{position:relative;height:53px;font-size:13px;line-height:19px;color:var(--body)}
.beliefs li::before{content:"";position:absolute;left:-26px;top:3px;width:12px;height:12px;border-radius:50%;background:var(--red)}
.beliefs li::after{content:"";position:absolute;left:-23px;top:6.5px;width:4px;height:4px;border-right:2px solid #fff;border-top:2px solid #fff;transform:rotate(45deg)}
.beliefs strong{display:block;color:var(--ink);font-weight:700}

/* Business lines */
.lines{top:1388px}
.card{position:absolute;top:169px;width:269px;height:403px;background:var(--card);border-radius:12px;padding:28px 26px}
.card h3{text-align:center;font-family:"Rubik",sans-serif;font-weight:500;font-size:24px;color:var(--ink);margin-bottom:22px}
.card p{font-size:9.6px;line-height:15.5px;text-align:justify;color:var(--muted);margin-bottom:14px}

/* Timeline */
.timeline-1{top:2062px}
.timeline-2{top:2737px}
.milestone{position:absolute;width:250px;text-align:center;transform:translateX(-50%)}
.photo{position:absolute;width:84px;height:84px;border-radius:50%;border:4px solid #f2d5d9;transform:translate(-50%,-50%);background:radial-gradient(circle at 40% 35%,#5b6f8e,#1d2638 70%)}
.year{position:absolute;transform:translateX(-50%);background:var(--red);color:#fff;font-family:"Rubik",sans-serif;font-weight:600;font-size:11px;padding:3px 12px;border-radius:12px}
.milestone h4{font-size:9.5px;line-height:14px;font-weight:700;color:var(--ink);text-transform:uppercase;margin-bottom:12px}
.milestone p{font-size:9.5px;line-height:15px;color:var(--body);margin-bottom:12px}

/* Where we are now */
.now{top:3411px}
.stat{position:absolute;width:300px;transform:translateX(-50%);text-align:center}
.stat .icon{width:76px;height:76px;margin:0 auto;border:2px solid #e2e2e6;border-radius:12px;box-shadow:0 2px 6px rgba(0,0,0,.08);display:flex;align-items:center;justify-content:center}
.stat .value{font-family:"Rubik",sans-serif;font-size:26px;color:var(--ink);margin-top:34px}
.stat .label{font-family:"Rubik",sans-serif;font-weight:500;font-size:17px;line-height:21px;color:var(--red)}

/* Thank you */
.thanks{top:4084px;background:linear-gradient(135deg,#5c1622,#a52a3b 45%,#6c1a27)}
.thanks-disc{position:absolute;left:207px;top:-10px;width:697px;height:697px;border-radius:50%;background:var(--white)}
.thanks .brand-lg{position:absolute;left:0;right:0;top:58px;text-align:center;font-family:"Rubik",sans-serif;font-weight:500;font-size:40px;color:var(--ink)}
.thanks h2{position:absolute;left:0;right:0;top:122px;text-align:center;font-family:"Rubik",sans-serif;font-weight:700;font-size:86px;color:#111}
.contact{position:absolute;left:389px;display:flex;align-items:center;gap:18px;font-family:"Rubik",sans-serif;font-size:22px;color:var(--ink);line-height:40px}
.contact svg{flex:none}
</style>
</head>
<body>

<!-- Slide 1: Welcome -->
<section class="slide welcome">
  <svg class="decor" viewBox="0 0 1110 623" aria-hidden="true">
    <path d="M0 0H690C600 140 520 320 515 623H0Z" fill="#fff" opacity=".95"/>
  </svg>
  <svg class="decor" viewBox="0 0 1110 623" role="img" aria-label="Photo of a modern multi-storey apartment building under a blue sky">
    <defs><linearGradient id="sky" x1="0" y1="0" x2="0" y2="1"><stop offset="0" stop-color="#8fb2d6"/><stop offset=".55" stop-color="#d9dde2"/><stop offset=".8" stop-color="#b9bdb8"/><stop offset="1" stop-color="#6f8a5e"/></linearGradient></defs>
    <path d="M0 0H680C590 140 512 320 506 623H0Z" fill="url(#sky)"/>
  </svg>
  <svg class="decor" viewBox="0 0 1110 623" aria-hidden="true">
    <path d="M690 0C600 140 520 320 515 623" fill="none" stroke="#fff" stroke-width="6"/>
  </svg>
  <div class="welcome-text">
    <div class="kicker">WELCOME TO</div>
    <div class="name">The Marnwick Group</div>
    <div class="tag">Providing innovative housing solutions nationwide.</div>
  </div>
  <div class="follow">Follow us <span class="rule"></span><span class="dot"></span><span class="dot"></span><span class="dot"></span></div>
</section>

<!-- Slide 2: Who We Are -->
<section class="slide who">
  <svg class="decor" viewBox="0 0 1110 623" aria-hidden="true">
    <defs><linearGradient id="corner" x1="0" y1="0" x2="1" y2="1"><stop offset="0" stop-color="#c42436"/><stop offset="1" stop-color="#7e0f1c"/></linearGradient></defs>
    <path d="M0 0H500C360 25 170 90 0 262Z" fill="url(#corner)"/>
    <path d="M0 275C170 100 360 30 520 0" fill="none" stroke="#c9cacc" stroke-width="3"/>
    <path d="M1110 320C1010 470 820 590 600 623H1110Z" fill="url(#corner)"/>
    <path d="M1110 300C1000 460 800 585 570 623" fill="none" stroke="#c9cacc" stroke-width="3"/>
  </svg>
  <div class="brand">The Marnwick Group</div>
  <h2 class="slide-title" style="top:64px">Who We Are</h2>
  <div class="divider" style="top:108px"><i></i><i></i><i></i></div>
  <p class="intro">The Marnwick Group develops and invests nationally in quality real estate projects across multiple business lines. We approach business through an entrepreneurial lens, cultivating a team who acts entrepreneurially and rewards team members commensurate with their contributions. This approach drives us to produce outsized returns.</p>
  <p class="lead">While what we do determines our day-to-day, it’s what we believe that makes us The Marnwick Group.</p>
  <ul class="beliefs">
    <li><strong>We believe in being action oriented.</strong>Results are achieved by compressing the distance between good ideas and great execution.</li>
    <li><strong>We believe in authenticity.</strong>It doesn’t take a suit and tie to solve big problems. Work hard and be yourself.</li>
    <li><strong>We believe in big goals.</strong>In order to achieve uncommon results, our goals must push us out of our comfort zone, beyond what we think is possible.</li>
    <li><strong>We believe we can do well while doing good.</strong>We give back to our communities and aim to have a lasting social impact.</li>
    <li><strong>We believe work and fun are not mutually exclusive.</strong>When done right, hard work can be a lot of fun.</li>
    <li><strong>We believe in a thoughtful approach</strong>We utilize our experience and a considered approach to make swift, reasoned and<br>forward-thinking decisions.</li>
  </ul>
</section>

<!-- Slide 3: Business Lines -->
<section class="slide lines">
  <svg class="decor" viewBox="0 0 1110 623" aria-hidden="true">
    <defs><linearGradient id="corner2" x1="0" y1="0" x2="1" y2="1"><stop offset="0" stop-color="#c42436"/><stop offset="1" stop-color="#7e0f1c"/></linearGradient></defs>
    <path d="M0 0H500C360 25 170 90 0 262Z" fill="url(#corner2)"/>
    <path d="M0 275C170 100 360 30 520 0" fill="none" stroke="#c9cacc" stroke-width="3"/>
    <path d="M1110 470C1000 560 840 610 700 623H1110Z" fill="url(#corner2)"/>
    <path d="M1110 450C990 550 820 605 660 623" fill="none" stroke="#c9cacc" stroke-width="3"/>
  </svg>
  <div class="brand">The Marnwick Group</div>
  <h2 class="slide-title" style="top:64px">Our Business Lines</h2>
  <div class="divider" style="top:108px"><i></i><i></i><i></i></div>
  <article class="card" style="left:123px">
    <h3>Marnwick Capital</h3>
    <p>Marnwick Capital is the group’s market rate investment vehicle founded on the basis of value investing philosophies, focusing on distressed, opportunistic, value-add and niche market real estate assets. Within these classes, Marnwick typically targets underperforming properties that often require significant renovations and hands-on management to realize the assets’ full potential.</p>
    <p>Marnwick constantly assesses market conditions and end-user demand in order to identify short- and long-term inefficiencies and arbitrage opportunities. Subsequent to identifying broader market opportunity, Marnwick applies a methodical approach to set the stage for realizing superior returns.</p>
  </article>
  <article class="card" style="left:419px">
    <h3>Marnwick Capital</h3>
    <p>In the context of a deepening affordability crisis, the group entered affordable housing in 2013 with the establishment of Marnwick Communities, a developer, owner, and operator focused on providing affordable housing nationwide.</p>
    <p>Through property-based Section 8 subsidies, Low Income Housing Tax Credits, and additional programs, Marnwick aims to preserve and expand long term housing affordability for low-income households. Marnwick and its principals have a proven track record in the industry for safeguarding and growing the number of affordable units throughout the country.</p>
  </article>
  <article class="card" style="left:718px">
    <h3>Marnwick Capital</h3>
    <p>Marnwick Impact Housing was founded to address the housing problem for middle income earners – moderate-income individuals that cannot afford to reside in the communities in which they work.</p>
    <p>Drawing upon the company’s affordable and market-rate housing expertise, Marnwick Impact Housing creates quality, income restricted housing units. The essential housing properties serve middle-income residents who earn incomes in excess of traditional affordable housing restrictions and yet cannot afford market rate housing without becoming rent burdened. The company undertakes these projects through strategic public-private partnerships with government agencies and financial institutions.</p>
  </article>
</section>

<!-- Slide 4: Timeline 2010–2013 -->
<section class="slide timeline-1">
  <svg class="decor" viewBox="0 0 1110 623" aria-hidden="true">
    <defs><linearGradient id="corner3" x1="0" y1="0" x2="1" y2="1"><stop offset="0" stop-color="#c42436"/><stop offset="1" stop-color="#7e0f1c"/></linearGradient></defs>
    <g fill="var(--bar)" opacity=".7">
      <rect x="230" y="520" width="80" height="103"/>
      <rect x="380" y="420" width="70" height="203"/>
      <rect x="520" y="340" width="70" height="283"/>
      <rect x="700" y="250" width="75" height="373"/>
      <rect x="880" y="180" width="80" height="443"/>
    </g>
    <path d="M30 600L460 280L560 330L1000 80" fill="none" stroke="var(--bar)" stroke-width="34" opacity=".8"/>
    <path d="M980 55L1040 70L1005 120Z" fill="var(--bar)" opacity=".8"/>
    <path d="M0 0H500C360 25 170 90 0 262Z" fill="url(#corner3)"/>
    <path d="M0 275C170 100 360 30 520 0" fill="none" stroke="#c9cacc" stroke-width="3"/>
    <path d="M40 165C160 210 300 160 410 164C520 168 600 210 685 197C800 180 880 120 958 145C1020 165 1070 170 1110 160" fill="none" stroke="#b8b8bd" stroke-width="1.5" stroke-dasharray="6 5"/>
  </svg>
  <div class="brand">The Marnwick Group</div>
  <h2 class="slide-title upper" style="top:52px">Company Timeline</h2>
  <div class="divider" style="top:96px"><i></i><i></i><i></i></div>

  <div class="photo" style="left:139px;top:191px" role="img" aria-label="City skyline at night"></div>
  <div class="year" style="left:139px;top:226px">2010</div>
  <div class="photo" style="left:410px;top:164px" role="img" aria-label="Aerial view of a city"></div>
  <div class="year" style="left:410px;top:199px">2010</div>
  <div class="photo" style="left:685px;top:197px" role="img" aria-label="Downtown skyscrapers"></div>
  <div class="year" style="left:685px;top:232px">2011</div>
  <div class="photo" style="left:958px;top:145px" role="img" aria-label="Looking up at glass towers"></div>
  <div class="year" style="left:958px;top:180px">2012-2013</div>

  <div class="milestone" style="left:139px;top:282px">
    <h4>What do you get when you combine a principal, an unpaid intern, and 5,000 square feet of borrowed office space? The beginning of Marnwick</h4>
    <p>In 2010, we found the Company based on value investing principals in the depths of the Great Financial Crisis with a focus on value-add, distressed and opportunistic investments. We leverage our significant experience and track record in the value-add institutional real estate investment space, starting small and building an investment firm from the ground up. It may not be the easiest path to choose, but we do what’s right and not what’s easy.</p>
  </div>
  <div class="milestone" style="left:410px;top:229px">
    <h4>Start with what you know</h4>
    <p>Finding a hidden gem, polishing it, and presenting it to the world can be a lot of fun. We know how to do it and enjoy doing it, so we decide to dive into the value-add apartment business. We find the worn out properties in great neighborhoods and we find the underutilized properties in the next hot neighborhoods. The key to success is to see things for what they can be, and not just what they are, then to innovate through reimaging, reorganizing and reworking.</p>
  </div>
  <div class="milestone" style="left:685px;top:282px">
    <h4>Who wouldn’t want to buy $1.00 for 70 cents?</h4>
    <p>Armed with a man at the court house steps with an earpod in one ear and millions of dollars of cashiers checks in his back pocket, we embark on a daily ritual of bidding on apartment building foreclosures. Through the Hollow Birch Fund, a discretionary investment fund we raise to bid on foreclosed, distressed apartments, we successfully invest in this space over a four year period. With no traditional diligence available for the properties, and just seconds to bid, it can be a nerve wracking experience, but we never lose money on any of the acquisitions, and actually earn quite an attractive return. If this isn’t a crash course in making swift, reasoned, and forward thinking decisions, we don’t know what is.</p>
  </div>
  <div class="milestone" style="left:958px;top:210px">
    <h4>Eureka!</h4>
    <p>After a nail biting 22 months of money going out the door during the Company’s initial existence, we successfully complete our first disposition of an investment which (thankfully) brings some profit back into the bank account. With a sale price 55% above our purchase, we’re off to a good start. And better yet, our investment thesis is validated.</p>
    <h4>Doing well while doing good.</h4>
    <p>After rigorous analysis we dip our toe in the affordable housing waters because of perceived opportunity. While the initial opportunity is just a sliver of the vast affordable housing landscape we uncover in the years to come, the affordable housing industry becomes more of a mission rather than just a mere opportunity. We create a new segment of the business, Marnwick Communities, to focus on fulfilling affordable housing needs across the country. This would not be possible without our pursuit of lifelong learning, allowing us to marry our existing multifamily experience.</p>
  </div>
</section>

<!-- Slide 5: Timeline 2015–2022 -->
<section class="slide timeline-2">
  <svg class="decor" viewBox="0 0 1110 623" aria-hidden="true">
    <defs><linearGradient id="corner4" x1="0" y1="0" x2="1" y2="1"><stop offset="0" stop-color="#c42436"/><stop offset="1" stop-color="#7e0f1c"/></linearGradient></defs>
    <g fill="var(--bar)" opacity=".7">
      <rect x="230" y="520" width="80" height="103"/>
      <rect x="380" y="420" width="70" height="203"/>
      <rect x="520" y="340" width="70" height="283"/>
      <rect x="660" y="270" width="75" height="353"/>
      <rect x="880" y="180" width="80" height="443"/>
    </g>
    <path d="M30 600L460 280L560 330L1000 80" fill="none" stroke="var(--bar)" stroke-width="34" opacity=".8"/>
    <path d="M980 55L1040 70L1005 120Z" fill="var(--bar)" opacity=".8"/>
    <path d="M0 0H500C360 25 170 90 0 262Z" fill="url(#corner4)"/>
    <path d="M0 275C170 100 360 30 520 0" fill="none" stroke="#c9cacc" stroke-width="3"/>
    <path d="M40 165C160 210 300 160 410 164C520 168 600 210 685 197C800 180 880 120 958 145C1020 165 1070 170 1110 160" fill="none" stroke="#b8b8bd" stroke-width="1.5" stroke-dasharray="6 5"/>
  </svg>
  <div class="brand">The Marnwick Group</div>
  <h2 class="slide-title upper" style="top:52px">Company Timeline</h2>
  <div class="divider" style="top:96px"><i></i><i></i><i></i></div>

  <div class="photo" style="left:139px;top:191px" role="img" aria-label="City skyline at night"></div>
  <div class="year" style="left:139px;top:226px">2015</div>
  <div class="photo" style="left:410px;top:164px" role="img" aria-label="Aerial view of a city"></div>
  <div class="year" style="left:410px;top:199px">2016</div>
  <div class="photo" style="left:685px;top:197px" role="img" aria-label="Downtown skyscrapers"></div>
  <div class="year" style="left:685px;top:232px">2017</div>
  <div class="photo" style="left:958px;top:145px" role="img" aria-label="Looking up at glass towers"></div>
  <div class="year" style="left:958px;top:180px">2021-2022</div>

  <div class="milestone" style="left:139px;top:280px">
    <h4>Ladies and gentlemen, start your engines.</h4>
    <p>While the debate still rages in the office as to who actually won the inaugural Marnwick go karting race, one thing is certain: we all walk away that day with big smiles on our faces. We work hard and have fun, otherwise, what’s the point?</p>
  </div>
  <div class="milestone" style="left:410px;top:232px">
    <h4>The Naked City</h4>
    <p>Just off the glittering Las Vegas strip we find what we believe to be an attractive affordable housing opportunity. But once we complete our diligence, we realize that the property has too many physical needs to be a viable long term investment. Rather than walking away, we decide to dive deeper into the affordable housing world by utilizing the Low Income Housing Tax Credit to complete a redevelopment of the 201 unit property located in a neighborhood known as The Naked City for its history as a home to many of Las Vegas’ showgirls in the 50’s and 60’s. This redevelopment not only enhances the lives of the property’s residents, but contributes to lifting the entire neighborhood. This is the first of many projects Marnwick Communities undertakes to redevelop affordable housing across the country.</p>
  </div>
  <div class="milestone" style="left:685px;top:285px">
    <h4>Ladies and gentlemen, start your engines.</h4>
    <p>While the debate still rages in the office as to who actually won the inaugural Marnwick go karting race, one thing is certain: we all walk away that day with big smiles on our faces. We work hard and have fun, otherwise, what’s the point?</p>
  </div>
  <div class="milestone" style="left:958px;top:210px">
    <h4>Don’t step in the kitchen</h4>
    <p>What company retreat is complete without a bit of work, a lot of laughs, and little competition? The competitive juices are in full swing at the first Marnwick pickleball tournament. The open courtside bar soothes the sting of defeat, but regardless of where we each rank in the standings, there is a lot of talk of pickleball becoming the new favorite Marnwick pastime.</p>
    <h4>Movin’ on up</h4>
    <p>The growth and success of a company does not happen overnight, nor does it just happen. It takes a team of dedicated, intelligent, results oriented individuals to deliver exceptional results. When a member of the team consistently delivers results, we reward those results. In this case, we name our first Partner.</p>
  </div>
</section>

<!-- Slide 6: Where Are We Now -->
<section class="slide now">
  <svg class="decor" viewBox="0 0 1110 623" aria-hidden="true">
    <defs><linearGradient id="corner5" x1="0" y1="0" x2="1" y2="1"><stop offset="0" stop-color="#c42436"/><stop offset="1" stop-color="#7e0f1c"/></linearGradient>
      <symbol id="bldg" viewBox="0 0 30 24"><rect x="2" y="8" width="7" height="14" fill="#b01a2b"/><rect x="11" y="2" width="8" height="20" fill="#b01a2b"/><rect x="21" y="10" width="7" height="12" fill="#b01a2b"/><rect x="13" y="5" width="2" height="2" fill="#fff"/><rect x="16" y="5" width="2" height="2" fill="#fff"/><rect x="13" y="10" width="2" height="2" fill="#fff"/><rect x="16" y="10" width="2" height="2" fill="#fff"/><rect x="4" y="12" width="3" height="2" fill="#fff"/><rect x="23" y="14" width="3" height="2" fill="#fff"/></symbol>
    </defs>
    <path d="M0 0H500C360 25 170 90 0 262Z" fill="url(#corner5)"/>
    <path d="M0 275C170 100 360 30 520 0" fill="none" stroke="#c9cacc" stroke-width="3"/>
  </svg>
  <div class="brand">The Marnwick Group</div>
  <h2 class="slide-title" style="top:62px">Where Are We Now</h2>
  <div class="divider" style="top:106px"><i></i><i></i><i></i></div>

  <div class="stat" style="left:177px;top:166px"><div class="icon"><svg width="30" height="24"><use href="#bldg"/></svg></div><div class="value">7,500 +</div><div class="label">Apartment Units<br>Acquired</div></div>
  <div class="stat" style="left:541px;top:166px"><div class="icon"><svg width="30" height="24"><use href="#bldg"/></svg></div><div class="value">Over $4 billion</div><div class="label">Senior Management Team<br>Acquisition Experience</div></div>
  <div class="stat" style="left:907px;top:166px"><div class="icon"><svg width="30" height="24"><use href="#bldg"/></svg></div><div class="value">$1+ billion</div><div class="label">Current Assets<br>Under</div></div>
  <div class="stat" style="left:177px;top:384px"><div class="icon"><svg width="30" height="24"><use href="#bldg"/></svg></div><div class="value">13,000+</div><div class="label">Number of<br>Residents Served</div></div>
  <div class="stat" style="left:541px;top:384px"><div class="icon"><svg width="30" height="24"><use href="#bldg"/></svg></div><div class="value">$60mm+</div><div class="label">Renovations<br>Performed</div></div>
  <div class="stat" style="left:907px;top:384px"><div class="icon"><svg width="30" height="24"><use href="#bldg"/></svg></div><div class="value">34.87%</div><div class="label">IRR of Realized Investments –<br>Marnwick Communities</div></div>
</section>

<!-- Slide 7: Thank You -->
<section class="slide thanks">
  <div class="decor" role="img" aria-label="Looking up at tall city towers, tinted red"></div>
  <div class="thanks-disc"></div>
  <div class="brand-lg">The Marnwick Group</div>
  <h2>Thank you</h2>
  <div class="contact" style="top:246px">
    <svg width="40" height="40" viewBox="0 0 40 40" aria-hidden="true"><circle cx="20" cy="20" r="18" fill="none" stroke="#b01a2b" stroke-width="3"/><path d="M14 11l4 1 1 5-2.5 1.5a11 11 0 0 0 5 5L23 21l5 1 1 4c-1 2-3 3-5 2.5C17 27 13 23 11.5 16 11 14 12 12 14 11z" fill="#b01a2b"/></svg>
    +1 888-888-8888
  </div>
  <div class="contact" style="top:342px">
    <svg width="40" height="40" viewBox="0 0 40 40" aria-hidden="true"><circle cx="20" cy="20" r="18" fill="none" stroke="#b01a2b" stroke-width="3"/><rect x="11" y="14" width="18" height="13" rx="1.5" fill="none" stroke="#b01a2b" stroke-width="2.5"/><path d="M11 15l9 7 9-7" fill="none" stroke="#b01a2b" stroke-width="2.5"/></svg>
    info@marnwickgroup.com
  </div>
  <div class="contact" style="top:426px;align-items:flex-start">
    <svg width="40" height="40" viewBox="0 0 40 40" aria-hidden="true"><circle cx="20" cy="20" r="18" fill="none" stroke="#b01a2b" stroke-width="3"/><path d="M20 30s-7-8-7-13a7 7 0 0 1 14 0c0 5-7 13-7 13z" fill="#b01a2b"/><circle cx="20" cy="17" r="2.6" fill="#fff"/></svg>
    <span>108 Lorem ipsum dolor sit<br>amet, consectetur</span>
  </div>
</section>

</body>
</html>
```